Brindlecove Business Card

Looking for a new business Card layout for our company, brindlecove.

Logo Text

Standard Business Card , Name, email, phone, website. www.brindlecove-example.com

```html
<!DOCTYPE html>
<html lang="en">
<head>
<meta charset="utf-8">
<title>Brindlecove Business Card</title>
<link rel="stylesheet" href="https://fonts.googleapis.com/css2?family=Exo+2:wght@300;400;800&display=swap">
<style>
  :root {
    --bg: #e9ebee;
    --paper: #ffffff;
    --slate: #5d6b80;
    --slate-dark: #4d5a6e;
    --sky: #45b4dc;
    --sky-light: #66c3e2;
    --sky-deep: #2fa3d6;
    --rim: #d4d8de;
    --ink: #5f6b7c;
  }
  * { margin: 0; padding: 0; box-sizing: border-box; }
  html, body { width: 1200px; height: 900px; overflow: hidden; }
  body {
    background: var(--bg);
    font-family: "Exo 2", sans-serif;
    display: flex;
    flex-direction: column;
    align-items: center;
    justify-content: center;
    gap: 54px;
  }
  .card {
    position: relative;
    width: 600px;
    height: 343px;
    background: var(--paper);
    overflow: hidden;
    box-shadow: 0 6px 18px rgba(40, 50, 70, 0.18);
  }
  .card-art { position: absolute; inset: 0; width: 100%; height: 100%; }
  .brand {
    position: absolute;
    display: flex;
    align-items: center;
    gap: 10px;
  }
  .brand-dot {
    width: 26px; height: 26px;
    border-radius: 50%;
    background: var(--slate);
  }
  .brand-name {
    font-weight: 800;
    font-size: 38px;
    letter-spacing: 0.5px;
    color: var(--sky);
    text-transform: uppercase;
    line-height: 1;
  }
  .card-back .brand { right: 40px; top: 150px; }
  .brand-url {
    position: absolute;
    right: 42px; top: 200px;
    font-size: 14px;
    font-weight: 300;
    letter-spacing: 2px;
    color: var(--ink);
  }
  .card-front .brand { right: 140px; top: 118px; }
  .person { position: absolute; left: 60px; top: 208px; }
  .person-role { font-size: 14px; font-weight: 300; color: var(--ink); }
  .person-name {
    font-size: 24px; font-weight: 400; color: var(--sky);
    text-transform: uppercase; line-height: 1.05;
  }
  .contact {
    position: absolute; left: 60px; top: 268px;
    list-style: none;
    font-size: 14px; font-weight: 300; color: var(--ink);
    line-height: 21px;
  }
  .contact b { color: var(--sky); font-weight: 800; margin-right: 4px; }
</style>
</head>
<body>

<section class="card card-back" aria-label="Card back">
  <svg class="card-art" viewBox="0 0 600 343" aria-hidden="true">
    <defs>
      <linearGradient id="slateFade" x1="0" y1="0" x2="1" y2="1">
        <stop offset="0" stop-color="var(--slate-dark)"/>
        <stop offset="1" stop-color="var(--slate)"/>
      </linearGradient>
    </defs>
    <path d="M0 0 H330 C340 70 300 100 240 100 L240 250 C300 255 345 300 335 343 H0 Z" fill="url(#slateFade)"/>
    <path d="M125 150 C120 95 190 80 255 100 C320 120 330 200 280 235 C235 265 135 255 125 195 Z" fill="var(--paper)" stroke="var(--rim)" stroke-width="4"/>
    <circle cx="-10" cy="325" r="80" fill="var(--paper)" stroke="var(--rim)" stroke-width="4"/>
  </svg>
  <div class="brand">
    <span class="brand-dot"></span>
    <span class="brand-name">Brindlecove</span>
  </div>
  <p class="brand-url">www.brindlecove-example.com</p>
</section>

<section class="card card-front" aria-label="Card front">
  <svg class="card-art" viewBox="0 0 600 343" aria-hidden="true">
    <defs>
      <linearGradient id="skyFade" x1="0" y1="0" x2="1" y2="1">
        <stop offset="0" stop-color="var(--sky-light)"/>
        <stop offset="1" stop-color="var(--sky-deep)"/>
      </linearGradient>
    </defs>
    <path d="M70 0 C100 70 170 100 235 95 C300 90 320 40 385 30 C445 22 475 65 472 125 C469 185 440 205 446 255 C452 300 480 330 505 343 H600 V0 Z" fill="url(#skyFade)"/>
    <path d="M70 0 C100 70 170 100 235 95 C300 90 320 40 385 30 C445 22 475 65 472 125 C469 185 440 205 446 255 C452 300 480 330 505 343" fill="none" stroke="var(--rim)" stroke-width="4"/>
    <circle cx="612" cy="35" r="62" fill="var(--paper)" stroke="var(--rim)" stroke-width="4"/>
  </svg>
  <div class="brand">
    <span class="brand-dot"></span>
    <span class="brand-name">Brindlecove</span>
  </div>
  <div class="person">
    <p class="person-role">Director</p>
    <p class="person-name">Mara Ellwood</p>
  </div>
  <ul class="contact">
    <li><b>T .</b>555-014-227</li>
    <li><b>E .</b>mara@brindlecove.com</li>
    <li><b>W.</b>www.brindlecove-example.com</li>
  </ul>
</section>

</body>
</html>
```